Thermal Camera flyer

We would like to obtain a sales orientated brochure to promote our two models of thermal imaging cameras as a response to the current Covid 19 health issues. I have provided the text, photos and detailed product specifications , in addition to a sample competitors brochure.
BROCHURE Details : 2 sided - front side to show product, its applications in business, school, hospitals, with text details - Back page to show specifications chart and contact information for Corvel Signal Works. (Melbourne -Sydney-Perth-Brisbane - 1300 647 519
Brochure should be "eye-catching" and reflect the product as a high quality, must-have technology device for todays world.

```html
<!DOCTYPE html>
<html lang="en">
<head>
<meta charset="utf-8">
<title>Thermal Camera Flyer – Corvel Signal Works</title>
<link rel="stylesheet" href="https://fonts.googleapis.com/css2?family=Alfa+Slab+One&family=Montserrat:wght@800&family=Roboto:wght@300;400&display=swap">
<style>
  :root{
    --bg-dark:#0b0b0c;
    --bg-mid:#2a2a2b;
    --bg-light:#5a5a5a;
    --accent-red:#e8344f;
    --spec-blue:#6aa7de;
    --bar-blue:#5b95cf;
    --brand-blue:#4a86c8;
    --text-light:#e4e4e4;
    --bracket-blue:#36b0e6;
    --thermal-purple:#5a2a9c;
    --thermal-magenta:#9a3391;
    --white:#ffffff;
  }
  *{margin:0;padding:0;box-sizing:border-box;}
  html,body{width:1200px;height:927px;overflow:hidden;background:var(--bg-dark);}
  .flyer{
    position:relative;width:1200px;height:927px;overflow:hidden;
    background:linear-gradient(150deg,var(--bg-dark) 0%,#151516 45%,var(--bg-mid) 75%,var(--bg-light) 100%);
    font-family:"Roboto",Arial,sans-serif;font-weight:300;color:var(--text-light);
  }
  .backdrop{position:absolute;inset:0;}

  .face-visual{position:absolute;left:38px;top:22px;width:238px;height:222px;}
  .face-visual .art{
    position:absolute;left:30px;top:10px;width:178px;height:206px;border-radius:18px;
    background:linear-gradient(180deg,#1b5f92 0%,#143e63 60%,rgba(12,22,36,0.2) 100%);
  }
  .face-visual svg{position:absolute;inset:0;}

  .intro{position:absolute;left:58px;top:254px;font-size:12.4px;line-height:21.3px;}

  .usage{position:absolute;left:55px;top:593px;width:320px;height:251px;border-left:5px solid var(--bar-blue);padding-left:14px;}
  .usage h2{font-family:"Alfa Slab One",Georgia,serif;font-weight:400;color:var(--accent-red);font-size:17.5px;line-height:22px;letter-spacing:.3px;margin-top:2px;}
  .usage p{font-size:12.4px;line-height:21.3px;margin-top:10px;white-space:nowrap;}

  .specs-title{position:absolute;left:384px;top:28px;font-family:"Alfa Slab One",Georgia,serif;font-weight:400;color:var(--accent-red);font-size:17px;letter-spacing:2.6px;}
  .specs-bar{position:absolute;left:384px;top:60px;width:6px;height:841px;background:var(--bar-blue);}

  .spec-table{position:absolute;display:grid;color:var(--spec-blue);font-size:12.3px;line-height:14.75px;}
  .spec-table .group{grid-column:1 / -1;font-size:12.6px;}
  .spec-table dt,.spec-table dd{white-space:nowrap;}
  .spec-camera{left:417px;top:58px;grid-template-columns:131px auto;}
  .spec-function{left:427px;top:499px;grid-template-columns:205px auto;}
  .spec-thermal{left:427px;top:734px;grid-template-columns:205px auto;line-height:15px;}
  .spec-thermal .group{margin-bottom:16px;}
  .spec-thermal .tall{align-self:end;}
  .spec-thermal .offset{padding-left:2px;}

  .call{position:absolute;left:631px;top:470px;font-family:"Montserrat",Arial,sans-serif;font-weight:800;color:var(--accent-red);font-size:42px;letter-spacing:.5px;white-space:nowrap;}

  .thermal-view{position:absolute;left:693px;top:-127px;width:536px;height:536px;border-radius:50%;
    background:linear-gradient(200deg,#7b3cbc 0%,var(--thermal-purple) 45%,var(--thermal-magenta) 100%);}
  .reticle{position:absolute;left:0;top:0;width:1200px;height:260px;pointer-events:none;}
  .reading{position:absolute;left:1010px;top:150px;width:74px;font-family:"Montserrat",Arial,sans-serif;font-weight:800;font-size:34px;color:var(--white);border-bottom:3px solid var(--white);line-height:46px;padding-left:3px;}

  .brand{position:absolute;left:920px;top:772px;}
  .brand .name{display:flex;align-items:center;gap:10px;font-family:"Roboto",Arial,sans-serif;font-weight:400;font-size:21px;color:var(--brand-blue);}
  .brand .mark{width:22px;height:22px;background:var(--brand-blue);}
  .brand .details{margin-top:24px;font-size:9.2px;letter-spacing:3.2px;line-height:21px;color:var(--white);font-weight:400;}
</style>
</head>
<body>
<main class="flyer">
  <svg class="backdrop" width="1200" height="927" viewBox="0 0 1200 927" aria-hidden="true">
    <defs>
      <linearGradient id="ring" x1="0" y1="0" x2="1" y2="1">
        <stop offset="0" stop-color="#1c1c1d"/>
        <stop offset=".55" stop-color="#3b3b3c"/>
        <stop offset="1" stop-color="#9a9a9a"/>
      </linearGradient>
      <linearGradient id="disc" x1="0" y1="0" x2="1" y2="1">
        <stop offset="0" stop-color="#060606"/>
        <stop offset=".7" stop-color="#111112"/>
        <stop offset="1" stop-color="#262627"/>
      </linearGradient>
    </defs>
    <circle cx="790" cy="240" r="610" fill="#161617"/>
    <circle cx="775" cy="262" r="490" fill="url(#ring)"/>
    <circle cx="770" cy="258" r="454" fill="none" stroke="#f2f2f2" stroke-width="3"/>
    <circle cx="770" cy="256" r="449" fill="url(#disc)"/>
    <circle cx="800" cy="250" r="470" fill="none" stroke="#2b2b2c" stroke-width="2" opacity=".8"/>
  </svg>

  <div class="face-visual">
    <div class="art" role="img" aria-label="Illustration of a head with a facial recognition wireframe mesh"></div>
    <svg width="238" height="222" viewBox="0 0 238 222" aria-hidden="true" fill="none" stroke="var(--bracket-blue)" stroke-width="2">
      <path d="M26 34V4H56"/><path d="M32 34V10H56"/>
      <path d="M206 4H236V34"/><path d="M206 10H230V34"/>
      <path d="M26 188V218H56"/><path d="M32 188V212H56"/>
      <path d="M236 188V218H206"/><path d="M230 188V212H206"/>
    </svg>
  </div>

  <p class="intro">The temperature<br>of your body is no longer<br>considered private information.<br>That’s the stance that businesses<br>&nbsp;around the world are taking as they<br>install thermal imaging cameras for<br>the safety of staff and visitors,<br>often equipped with facial recognition<br>technology, in their buildings in an<br>attempt<br>to cope with the COVID-19 pandemic.<br>It’s a movement one might call the<br>automation<br>of temperature checks.</p>

  <section class="usage">
    <h2>WHERE AND HOW<br>CAN IT BE USED ?</h2>
    <p>This Camera can be used with access control<br>gates. It is used in office buildings, schools, hotels,<br>hospitality, in fact, any space where Covid is<br>potentially a threat to staff or visitors.<br>Our Thermal Scanning &amp; Faciall Recognition<br>Camera is used as a safety and security measure.<br>If someone gets sick and takes legal action, you can<br>demonstrate that you have made your best effort to<br>protect your staff and visitors.</p>
  </section>

  <div class="thermal-view" role="img" aria-label="Thermal camera photo of two seated people"></div>
  <svg class="reticle" width="1200" height="260" viewBox="0 0 1200 260" aria-hidden="true" stroke="var(--white)" stroke-width="2.5" fill="none">
    <line x1="803" y1="41" x2="856" y2="41"/><line x1="876" y1="41" x2="927" y2="41"/>
    <line x1="866" y1="0" x2="866" y2="31"/><line x1="866" y1="51" x2="866" y2="102"/>
    <circle cx="866" cy="41" r="10"/>
  </svg>
  <div class="reading">37,5</div>

  <h1 class="specs-title">TECHNICAL SPECIFICATIONS</h1>
  <div class="specs-bar"></div>

  <dl class="spec-table spec-camera">
    <dt class="group">Model CS-08Camera</dt>
    <dt class="group">Camera</dt>
    <dt>Resolution:</dt><dd>2 million pixels</dd>
    <dt>Type:</dt><dd>Binocular wide dynamic camera</dd>
    <dt>Aperture:</dt><dd>F2.4</dd>
    <dt>Focusing distance:</dt><dd>50-150cm</dd>
    <dt>White balance:</dt><dd>auto</dd>
    <dt>Photo flood light:</dt><dd>LED and IR dual photo flood light</dd>
    <dt class="group">Screen</dt>
    <dt class="group">Screen</dt>
    <dt>Size:</dt><dd>8.0 inch IPS LCD screen</dd>
    <dt>Resolution:</dt><dd>800×1280</dd>
    <dt>Touch:</dt><dd>Not supported</dd>
    <dt class="group">Processor</dt>
    <dt class="group">Processor</dt>
    <dt>CPU:</dt><dd>QS3288 quad -core</dd>
    <dt>Storage:</dt><dd>EMMC 8G</dd>
    <dt class="group">Interface</dt>
    <dt class="group">Interface</dt>
    <dt>Network module:</dt><dd>Ethernet and wireless (WIFI)</dd>
    <dt>Audio:</dt><dd>2.5W / 4R speakers</dd>
    <dt>USB:</dt><dd>1 USB OTG, 1 USB HOST standard A port</dd>
    <dt>Serial communication:</dt><dd>1 RS232 serial port</dd>
    <dt>Relay output:</dt><dd>1 door open signal output</dd>
    <dt>Wiegand One Wiegand:</dt><dd>26/34 output, one Wiegand 26/34 input</dd>
    <dt>Upgrade button:</dt><dd>Support Uboot upgrade button</dd>
    <dt>Wired network:</dt><dd>1 RJ45 Ethernet socket</dd>
  </dl>

  <div class="call">CALL 1300 647 519</div>

  <dl class="spec-table spec-function">
    <dt class="group">Function</dt>
    <dt class="group">Function</dt>
    <dt>Face Detection:</dt><dd>Supports facial detection</dd>
    <dt>Face library:</dt><dd>Up to 30,000</dd>
    <dt>1: N face recognition:</dt><dd>Support</dd>
    <dt>1:1 face comparison:</dt><dd>Support</dd>
    <dt>Stranger detection:</dt><dd>Support</dd>
    <dt>Identify distance configuration:</dt><dd>Support</dd>
    <dt>UI interface configuration:</dt><dd>Support</dd>
    <dt>Upgrade remotely:</dt><dd>Support</dd>
    <dt>Interface:</dt><dd>Interfaces include device management, personnel /<br>photo management, record query, etc.</dd>
    <dt>Deployment method:</dt><dd>Support public cloud deployment, privatized<br>deployment, LAN use, stand &nbsp; -alone use</dd>
  </dl>

  <dl class="spec-table spec-thermal">
    <dt class="group">Infrared Imaging Thermal Module</dt>
    <dt>Temperature detection:</dt><dd>Support</dd>
    <dt>Temperature detection distance:</dt><dd>1 meter (optimal distance 0.5 meter)</dd>
    <dt>Temperature:</dt><dd>≤ &nbsp;±0.5°C measurement accuracy</dd>
    <dt>Temperature measurement range:</dt><dd>10°C~42°C</dd>
    <dt>Pixels:</dt><dd class="offset">32 X 32 dots (total 1024 pixels)</dd>
    <dt>Visitors' temperature is<br>normal and released<br>directly:</dt><dd class="tall offset">Support</dd>
    <dt>Abnormal temperature alarm:</dt><dd class="offset">Support (temperature alarm value can be set)</dd>
  </dl>

  <footer class="brand">
    <div class="name"><span class="mark"></span>Corvel Signal Works</div>
    <p class="details">Corvel Signal Works<br>MELBURNE-SYDNEY-PERT=BRISBANE<br>1300 647 519</p>
  </footer>
</main>
</body>
</html>
```